Thankyou post card for our customers

we would like to have a design for a post card that we would like to send to our customers once they have hired from us to say thankyou and to offer them a discount on there next hire.

our business is called Wattlebrook Caravan Rentals.
we hire our camper trailers and are based in Australia so alot of our customers go to the outback bush, beach etc with our campers.
the post card dimesions are
Full Bleed Size

213 x 98 mm
2517 x 1158 pixels

Document Trim Size

210 x 95 mm
2481 x 1122 pixels

I want 4 lines for the name and address on the right have side of the post card (like normal post cards have

Requirements
Must have
• we want it to be double sided so a Design on front and back of post card
I have attached our logo and some other things we have used in previous business material up to you if you want to use what I have uploaded

please note the logo with sunset I have attached I do not want the round logo used just wanted to show you how great the sunset looks we have changed our logo to just be the Wattlebrook Caravan Rentals but wouldnt mind if you used a sunset like this on the whole of the card? but not limited to that.

front of card:
our logo on front page (which is just the Wattlebrook Caravan Rentals attachement WCR1)
and our details:
P: 0491 326 715
W: www.wattlebrookcaravanrentals.com.au
E:info@wattlebrookcaravanrentals.com.au

and the following to be on the front of the post card:

Dear Fellow Campers,
We hope you have arrived home safely, and are rested and relaxed from your trip away. It was our pleasure to have you hire one of our campers and would like to thankyou for your support, we trust you enjoyed glamping and would like to think you would hire from us again. to show our appreciation we would like to offer you a 20% discount on any minimum 7 day hire over the next 6 months. we look forward to hearing from you again soon.
sincerely,
Gareth & Colby

offer not valid in peak period or in conjuction with any other offer

Full Bleed Size

213 x 98 mm
2517 x 1158 pixels

Document Trim Size

210 x 95 mm
2481 x 1122 pixels

Back of Card:

I want "Thankyou" written at top and then how ever else you design it

```html
<!DOCTYPE html>
<html lang="en">
<head>
<meta charset="utf-8">
<title>Wattlebrook Caravan Rentals – Thank You Postcard</title>
<link href="https://fonts.googleapis.com/css2?family=Handlee&family=Open+Sans:wght@400;600&display=swap" rel="stylesheet">
<style>
  :root {
    --backdrop: #d9d4cb;
    --card: #ffffff;
    --ink: #1a1a1a;
    --ink-soft: #333333;
    --line: #777777;
    --white: #ffffff;
    --sky-deep: #23418f;
    --sky-mid: #4d6db0;
    --dusk: #9a8fb5;
    --glow-pink: #e8707a;
    --glow-orange: #f39a3c;
    --glow-gold: #f3b634;
    --ground-dark: #1c1412;
    --pale-sky: #c9d4dc;
    --haze: #e6d6c8;
    --peach: #e9c3a3;
    --range: #7b6f70;
    --plain: #3a2e2c;
  }
  * { box-sizing: border-box; margin: 0; padding: 0; }
  html, body { width: 1200px; height: 1000px; overflow: hidden; }
  body { background: var(--backdrop); position: relative; font-family: "Open Sans", Arial, sans-serif; }

  .postcard {
    position: absolute;
    width: 960px;
    height: 435px;
    background: var(--card);
    overflow: hidden;
    box-shadow: 0 2px 8px rgba(0,0,0,0.18);
  }
  .postcard--front { left: 40px; top: 45px; }
  .postcard--back { left: 125px; top: 510px; }

  /* Front */
  .sunset-photo {
    position: absolute; left: 0; top: 0; width: 680px; height: 100%;
    background: linear-gradient(180deg, var(--sky-deep) 0%, var(--sky-mid) 30%, var(--dusk) 50%, var(--glow-pink) 64%, var(--glow-orange) 74%, var(--glow-gold) 79%, var(--ground-dark) 86%, #0e0b0b 100%);
    -webkit-mask-image: linear-gradient(90deg, #000 0%, #000 68%, transparent 100%);
    mask-image: linear-gradient(90deg, #000 0%, #000 68%, transparent 100%);
  }
  .welcome-letter {
    position: absolute; left: 52px; top: 62px; width: 420px;
    font-family: "Handlee", cursive;
    color: var(--white);
    font-size: 14.5px; line-height: 21px;
    transform: rotate(-4deg); transform-origin: left top;
  }
  .welcome-letter p + p { margin-top: 18px; }
  .welcome-letter .greeting { margin-bottom: 18px; }
  .front-contact {
    position: absolute; left: 72px; bottom: 18px;
    color: var(--white); font-size: 14px; letter-spacing: 0.2px;
  }
  .front-contact .divider { margin: 0 10px; }
  .front-web {
    position: absolute; right: 58px; top: 115px;
    font-size: 13px; font-weight: 600; color: var(--ink);
  }
  .front-brand {
    position: absolute; right: 52px; top: 165px; width: 420px;
    text-align: right;
    font-weight: 600; font-size: 42px; line-height: 50px;
    color: var(--ink); text-transform: uppercase;
  }

  /* Back */
  .outback-photo {
    position: absolute; left: 0; top: 0; width: 500px; height: 100%;
    background: linear-gradient(180deg, var(--pale-sky) 0%, var(--haze) 45%, var(--peach) 62%, var(--range) 70%, var(--plain) 78%, #241c1b 100%);
  }
  .thanks-title {
    position: absolute; left: 0; top: 62px; width: 500px;
    text-align: center;
    font-family: "Handlee", cursive;
    font-size: 76px; line-height: 1; color: var(--ink);
  }
  .offer-line {
    position: absolute; left: 0; top: 182px; width: 500px;
    text-align: center; font-size: 19px; color: var(--ink);
  }
  .offer-note {
    position: absolute; left: 0; top: 210px; width: 500px;
    text-align: center; font-size: 8px; color: var(--ink-soft);
  }
  .offer-terms {
    position: absolute; right: 482px; bottom: 10px;
    font-size: 8.5px; color: var(--white);
  }
  .back-brand {
    position: absolute; left: 552px; top: 48px;
    font-weight: 600; font-size: 20px; line-height: 24px;
    color: var(--ink); text-transform: uppercase; width: 240px;
  }
  .stamp-box {
    position: absolute; right: 48px; top: 22px;
    width: 80px; height: 80px; border: 1.5px solid var(--line);
  }
  .address-lines { position: absolute; left: 565px; top: 225px; }
</style>
</head>
<body>

  <section class="postcard postcard--front" aria-label="Postcard front">
    <div class="sunset-photo" role="img" aria-label="Outback sunset over a desert plain with a ute towing a camper trailer"></div>

    <div class="welcome-letter">
      <p class="greeting">Dear Fellow Campers,</p>
      <p>We hope you have arrived home safely, and are rested and relaxed from your trip away. It was our pleasure to have you hire one of our campers and would like to thankyou for your support, we trust you enjoyed glamping and would like to think you would hire from us again. to show our appreciation we would like to offer you a 20% discount on any minimum 7 day hire over the next 6 months. we look forward to hearing from you again soon.</p>
      <p>sincerely,<br>Gareth &amp; Colby</p>
    </div>

    <p class="front-contact">OUR CONTACT : 0491 326 715<span class="divider">|</span>info@wattlebrookcaravanrentals.com.au</p>

    <p class="front-web">www.wattlebrookcaravanrentals.com.au</p>
    <h1 class="front-brand">Wattlebrook Caravan Rentals</h1>
  </section>

  <section class="postcard postcard--back" aria-label="Postcard back">
    <div class="outback-photo" role="img" aria-label="Camper trailer on a ute parked at dusk overlooking a desert range"></div>

    <h2 class="thanks-title">“Thank You”</h2>
    <p class="offer-line">“You get 15% discount on next hire*”</p>
    <p class="offer-note">- with bring this post card -</p>
    <p class="offer-terms">*offer not valid in peak period or in conjuction with any other offer</p>

    <p class="back-brand">Wattlebrook Caravan Rentals</p>
    <div class="stamp-box" aria-label="Stamp"></div>

    <svg class="address-lines" width="340" height="170" viewBox="0 0 340 170" aria-label="Address lines">
      <line x1="2" y1="18" x2="325" y2="0" stroke="#777" stroke-width="1.5"/>
      <line x1="2" y1="65" x2="325" y2="47" stroke="#777" stroke-width="1.5"/>
      <line x1="2" y1="112" x2="325" y2="94" stroke="#777" stroke-width="1.5"/>
      <line x1="2" y1="159" x2="325" y2="141" stroke="#777" stroke-width="1.5"/>
    </svg>
  </section>

</body>
</html>
```